Conceptual Model Diagram for Replacing Medication with Behavior to Support Weight Loss Maintenance

Design a figure of a conceptual model that needs to be inserted into a word document for a QDV grant. This conceptual model illustrates how behavioral strategies can replace the regulatory functions lost after AOM discontinuation. The intervention targets three core vulnerabilities—appetite resurgence, metabolic inflexibility, and suboptimal mindstate—through the domains of Food, Physical Activity, and Mind. Sustained weight loss maintenance occurs at the intersection of these domains. The intervention is delivered within a design framework that makes behaviors easier to perform, aligns them with identity, and reinforces them through virtual support and community, ensuring real-world feasibility and long-term adherence.
Target Market(s)
QDV reviewers
Industry/Entity Type
academic
Font styles to use
Other font styles liked:
- arial
Requirements
Must have
- see my attached description

```html
<!DOCTYPE html>
<html lang="en">
<head>
<meta charset="utf-8">
<title>Conceptual Model – Behavior Replacing Medication for Weight Loss Maintenance</title>
<link rel="stylesheet" href="https://fonts.googleapis.com/css2?family=Arimo:wght@700&family=Alfa+Slab+One&family=Roboto+Condensed:wght@400&display=swap">
<style>
  :root {
    --green: #48fd8b;
    --green-deep: #3bf572;
    --green-soft: #80f8b4;
    --teal-text: #2ea37c;
    --white: #ffffff;
    --shadow: rgba(40, 40, 40, 0.75);
  }
  html, body {
    margin: 0;
    padding: 0;
    width: 1200px;
    height: 1200px;
    overflow: hidden;
    background: var(--white);
  }
  .model-canvas {
    display: block;
    width: 1200px;
    height: 1200px;
  }
  .card-frame {
    fill: var(--white);
    stroke: var(--green);
    stroke-width: 4;
    filter: drop-shadow(6px 6px 4px var(--shadow));
  }
  .pill { fill: var(--green); }
  .pill-text {
    font-family: "Arimo", Arial, sans-serif;
    font-weight: 700;
    fill: var(--white);
    text-anchor: middle;
  }
  .headline-text { font-size: 31px; letter-spacing: 0.5px; }
  .vulnerability-text { font-size: 30px; }
  .soft-arrow { fill: var(--green-soft); }
  .connector {
    fill: none;
    stroke: var(--green);
    stroke-width: 8;
    stroke-linejoin: round;
  }
  .arrow-head { fill: var(--green); }
  .domain-circle {
    fill: var(--green);
    stroke: var(--white);
    stroke-width: 4;
  }
  .core-triangle {
    fill: var(--green-deep);
    stroke: var(--white);
    stroke-width: 4;
    stroke-linejoin: round;
  }
  .domain-label {
    font-family: "Alfa Slab One", "Rockwell", serif;
    fill: var(--white);
  }
  .core-label {
    font-family: "Alfa Slab One", "Rockwell", serif;
    fill: var(--white);
    font-size: 17px;
    text-anchor: middle;
  }
  .framework-loop {
    fill: none;
    stroke: var(--green);
    stroke-width: 16;
    stroke-linecap: round;
  }
  .framework-label {
    font-family: "Arimo", Arial, sans-serif;
    font-weight: 700;
    font-size: 30px;
    fill: var(--green);
    text-anchor: middle;
  }
  .summary-text {
    font-family: "Roboto Condensed", "Arial Narrow", sans-serif;
    font-size: 38px;
    fill: var(--teal-text);
    text-anchor: middle;
  }
</style>
</head>
<body>
<svg class="model-canvas" viewBox="0 0 1920 1920" xmlns="http://www.w3.org/2000/svg" role="img" aria-label="Conceptual model: behavioral strategies replace regulatory function lost after AOM discontinuation">
  <!-- Card -->
  <rect class="card-frame" x="573" y="430" width="796" height="1060"/>

  <!-- Headline -->
  <rect class="pill" x="646" y="473" width="654" height="96" rx="48"/>
  <text class="pill-text headline-text" x="973" y="512">Behavioral strategies replace regulatory</text>
  <text class="pill-text headline-text" x="973" y="548">function lost after AOM discontinuation</text>

  <!-- Soft arrows from headline -->
  <g class="soft-arrows">
    <path class="soft-arrow" d="M724 569 h20 v18 h10 l-20 18 l-20 -18 h10 z"/>
    <path class="soft-arrow" d="M962 569 h20 v18 h10 l-20 18 l-20 -18 h10 z"/>
    <path class="soft-arrow" d="M1202 569 h20 v18 h10 l-20 18 l-20 -18 h10 z"/>
  </g>

  <!-- Vulnerabilities -->
  <rect class="pill" x="646" y="612" width="201" height="80" rx="40"/>
  <text class="pill-text vulnerability-text" x="750" y="646">Appetite</text>
  <text class="pill-text vulnerability-text" x="750" y="678">Resurgence</text>

  <rect class="pill" x="872" y="612" width="201" height="80" rx="40"/>
  <text class="pill-text vulnerability-text" x="973" y="646">Metabolic</text>
  <text class="pill-text vulnerability-text" x="973" y="678">Inflexibility</text>

  <rect class="pill" x="1099" y="612" width="201" height="80" rx="40"/>
  <text class="pill-text vulnerability-text" x="1201" y="646">Suboptimal</text>
  <text class="pill-text vulnerability-text" x="1201" y="678">Mindstate</text>

  <!-- Connectors to domains -->
  <path class="connector" d="M734 692 V714 Q734 726 746 726 H808 Q822 726 822 740 V752"/>
  <path class="arrow-head" d="M810 750 h24 l-12 18 z"/>
  <path class="connector" d="M967 692 V734"/>
  <path class="arrow-head" d="M955 732 h24 l-12 16 z"/>
  <path class="connector" d="M1200 692 V714 Q1200 726 1188 726 H1144 Q1132 726 1132 738 V746"/>
  <path class="arrow-head" d="M1120 744 h24 l-12 17 z"/>

  <!-- Domains -->
  <circle class="domain-circle" cx="898" cy="861" r="101"/>
  <circle class="domain-circle" cx="1047" cy="861" r="101"/>
  <circle class="domain-circle" cx="972" cy="982" r="101"/>
  <path class="core-triangle" d="M972 790 L1075 961 L870 961 Z"/>

  <text class="domain-label" x="817" y="838" font-size="23">Physical</text>
  <text class="domain-label" x="817" y="864" font-size="23">Activity</text>
  <text class="domain-label" x="1082" y="850" font-size="30" text-anchor="middle">Food</text>
  <text class="domain-label" x="975" y="1013" font-size="30" text-anchor="middle">Mind</text>

  <text class="core-label" x="972" y="896">Sustained</text>
  <text class="core-label" x="972" y="917">Weight Loss</text>
  <text class="core-label" x="972" y="937">Maintenance</text>

  <!-- Design framework loop -->
  <path class="framework-loop" d="M742 998 C690 1040 690 1110 760 1140 C860 1195 1080 1195 1180 1140 C1250 1110 1250 1040 1198 998"/>
  <path class="arrow-head" d="M766 975 L757 1000 L732 990 Z"/>
  <path class="arrow-head" d="M1178 975 L1208 990 L1183 1000 Z"/>
  <text class="framework-label" x="976" y="1129">Design Framework</text>

  <!-- Bracket arrows -->
  <path class="connector" d="M865 1226 V1260 Q865 1272 878 1272 L956 1273 Q970 1275 970 1290 V1315"/>
  <path class="connector" d="M1079 1226 V1260 Q1079 1272 1066 1272 L984 1273 Q970 1275 970 1290"/>
  <path class="arrow-head" d="M853 1228 h24 l-12 -18 z"/>
  <path class="arrow-head" d="M1067 1228 h24 l-12 -18 z"/>

  <!-- Summary -->
  <text class="summary-text" x="971" y="1362">Targets three core vulnerabilities through the</text>
  <text class="summary-text" x="971" y="1408">domains od Food, Physical Activity, and Mind</text>
  <text class="summary-text" x="971" y="1454">ensuring real-world feasibility and community</text>
</svg>
</body>
</html>
```